Creative, Modern and Conversion based Web Design

Kolvex Digital has recently launched a new logo and as part of our companies rebranding, we need a new website aimed towards the UK B2B marketplace.

The website needs to deliver a modern and creative website design whilst ensuring the design is tailored towards conversion optimisation.

This site must drive point of contact either from an online form, via a direct telephone call or Skype connection.

Our sales are all offline so the website will be a simple, elegant and stunning information portal.

Kolvex Digital offers Digital Marketing services to companies throughout the UK - our target audiences are companies that turnover a minimum of 3 million pounds a year and as such we need to deliver a professional image that installs confidence in our companies abilities.

We do not like websites that are reliant upon stock photography - we are happy for stock photography to be used in a small way however the site must not look like a template filled with stock photography.

What do we do

We supply digital marketing services to those companies who demand a strong return on investment - our company prides itself on delivering successful campaigns that help establish long-term profitable relationships.

A lot of the information presented on our old site is relevant today however the design sucks. So please use the information on our current website as a foundation for your design content.

I am looking for several page designs including

"Home Page" Desktop Version
"Service Page" Desktop Version
"Blog Page" Desktop Version

"Home Page" Mobile Version
"Service Page" Mobile Version
"Blog Page" Mobile Version

In the 1st instance please only submit a single design for the "Home Page" Desktop Version - those designers that we are impressed with will be asked to complete the other designs before a winner is selected.

I like modern clean fonts - the site needs to welcome the reader and encourage them to absorb the information - not to overload and make them leave.

The site must be designed to naturally fit our companies new logo.

NO TEMPLATES

Target Market(s)

B2b - 3 million turnover and above

Industry/Entity Type

Digital Marketing

Number of Pages Required

3 page

Requirements
Must have
• Blended well with the companies logo
• We need conversion optimisation to be a huge part of the design - we considered a conversation when a potential customer reaches out to use via - web form, telephone or skype
• The current content on the old website fits today's business but the design sucks.
• www.kolvexdigital-example.com
Nice to have
• We need 3 pages (in 2 variants Desktop and Mobile)
• Home Page
• Service Page
• Blog Page
• Please only deliver the "Home Page" desktop version - if we are happy with your design we will aks for the additional pages
Should not have
• No templates and not stock photo heavy design

```html
<!DOCTYPE html>
<html lang="en">
<head>
<meta charset="utf-8">
<title>Kolvex Digital – Search Marketing That Delivers</title>
<link rel="stylesheet" href="https://fonts.googleapis.com/css2?family=Alegreya+Sans:wght@500;700;800&family=Lato:ital,wght@0,400;0,700;0,900;1,400&display=swap">
<style>
:root{
  --blue:#1456a0;
  --blue-dark:#0e3f78;
  --navy:#14233a;
  --ink:#222831;
  --text:#555b63;
  --muted:#8a9099;
  --grey-bg:#efefef;
  --line:#d6d9dd;
  --white:#ffffff;
}
*{box-sizing:border-box;margin:0;padding:0}
html,body{width:1200px;height:4018px;overflow:hidden}
body{position:relative;background:var(--white);font-family:'Lato',sans-serif;color:var(--text)}
.abs{position:absolute}
.heading{font-family:'Alegreya Sans',sans-serif;font-weight:700;color:var(--ink)}
.btn{position:absolute;display:flex;align-items:center;justify-content:center;gap:16px;background:var(--blue);color:var(--white);font-family:'Lato',sans-serif;font-weight:900;font-size:17px;letter-spacing:.3px;text-transform:uppercase}
.btn.light{background:var(--white);color:var(--blue)}
.btn svg{width:22px;height:16px}

/* Hero */
.hero{left:0;top:0;width:1200px;height:651px;overflow:hidden}
.hero-photo{left:0;top:0;width:1200px;height:651px;background:linear-gradient(120deg,#3c4858 0%,#26303e 40%,#4d4a46 70%,#2e3440 100%)}
.hero-tint{left:0;top:0;width:1200px;height:651px;background:rgba(18,28,44,.55)}
.brand{left:75px;top:26px;display:flex;align-items:center;gap:12px;color:var(--white);font-family:'Lato',sans-serif;font-weight:900;font-size:26px;letter-spacing:.5px}
.brand-mark{width:26px;height:26px;background:var(--white)}
.nav{right:76px;top:44px;display:flex;gap:38px}
.nav a{color:var(--white);text-decoration:none;font-size:14px;text-transform:uppercase;letter-spacing:.4px;position:relative;padding-bottom:14px}
.nav a.active::after{content:"";position:absolute;left:0;right:0;bottom:0;height:2px;background:var(--blue)}
.hero-title{left:0;width:1200px;top:262px;text-align:center;color:var(--white);font-family:'Lato',sans-serif;font-weight:900;font-size:42px;line-height:58px;letter-spacing:.5px;text-transform:uppercase}
.hero-sub{left:0;width:1200px;top:405px;text-align:center;color:var(--white);font-size:17px}

/* Welcome */
.welcome-photo{left:0;top:651px;width:1200px;height:541px;background:linear-gradient(135deg,#c9ccd1 0%,#8d96a2 45%,#5b6470 75%,#a6abb2 100%);clip-path:polygon(800px 0,1200px 0,1200px 541px,563px 541px)}
.welcome-title{left:80px;top:752px;font-size:38px}
.lead{font-style:italic;color:#6f7680;font-size:17px;line-height:26px}
.welcome-lead{left:80px;top:822px;width:500px}
.body-copy{font-size:14px;line-height:25px;color:var(--text)}
.welcome-copy{left:80px;top:893px;width:500px}

/* Services */
.grey-band{left:0;top:1960px;width:1200px;height:560px;background:var(--grey-bg);clip-path:polygon(0 0,1200px 0,1200px 430px,0 560px)}
.services{left:54px;top:1197px;width:1093px;height:799px;background:var(--blue)}
.services-title{left:0;width:1093px;top:48px;text-align:center;color:var(--white);font-size:38px}
.service{width:330px;text-align:center;color:var(--white)}
.service svg{width:60px;height:60px;display:block;margin:0 auto 18px}
.service h3{font-family:'Lato',sans-serif;font-weight:400;font-size:20px;margin-bottom:12px}
.service p{font-size:14px;line-height:25px;color:#e6eef8;padding:0 6px}

/* Handle SEO */
.seo-title{left:80px;top:2080px;font-size:38px}
.seo-lead{left:80px;top:2138px;width:540px}
.seo-copy{left:80px;top:2182px;width:540px}
.screen-shot{left:685px;top:2088px;width:436px;height:300px;background:linear-gradient(135deg,#2b3442 0%,#465160 55%,#6c7480 100%)}

/* How it works */
.how-title{left:0;width:1200px;top:2524px;text-align:center;font-size:38px}
.step{width:340px;text-align:center}
.step-icon{position:relative;width:94px;height:94px;margin:0 auto 26px;border:1px solid var(--line);background:var(--white);display:flex;align-items:center;justify-content:center}
.step-icon svg{width:50px;height:50px}
.step-num{position:absolute;left:-8px;top:-12px;width:22px;height:22px;background:var(--blue);color:var(--white);font-size:13px;font-weight:700;display:flex;align-items:center;justify-content:center}
.step h3{font-family:'Lato',sans-serif;font-weight:400;font-size:20px;color:var(--ink);margin-bottom:12px}
.step p{font-size:14px;line-height:24px;color:var(--text)}
.step a{display:inline-block;margin-top:14px;font-size:14px;font-weight:700;color:var(--blue);text-decoration:underline}

/* Partners + CTA */
.cta{left:0;top:3014px;width:1200px;height:367px;background:linear-gradient(110deg,#3a3f47 0%,#23272e 45%,#4a4a4a 100%)}
.cta-tint{left:0;top:3014px;width:1200px;height:367px;background:rgba(20,24,32,.55)}
.partners{left:80px;top:2952px;width:1040px;height:129px;background:var(--white);box-shadow:0 4px 14px rgba(0,0,0,.12);display:flex;align-items:center;justify-content:space-around;padding:0 30px}
.badge{height:40px;background:#b9bdc3}
.cta-title{left:0;width:1200px;top:3148px;text-align:center;color:var(--white);font-size:40px}
.cta-sub{left:0;width:1200px;top:3212px;text-align:center;color:var(--white);font-size:17px}

/* Contact */
.contact-title{left:0;width:1200px;top:3430px;text-align:center;font-size:38px}
.field{border:1px solid var(--line);background:var(--white);font-size:13px;color:var(--muted);padding:14px 18px}

/* Footer */
.footer{left:0;top:3879px;width:1200px;height:139px;background:var(--blue)}
.footer-nav{left:0;width:1200px;top:44px;display:flex;justify-content:center;gap:22px;color:var(--white);font-size:14px}
.footer-nav span.sep{opacity:.7}
.copyright{left:0;width:1200px;top:86px;text-align:center;color:var(--white);font-size:14px}
</style>
</head>
<body>

<!-- Hero -->
<section class="hero abs">
  <div class="hero-photo abs" role="img" aria-label="Photo of a team working at laptops in a bright office"></div>
  <div class="hero-tint abs"></div>
  <div class="brand abs"><span class="brand-mark"></span>Kolvex Digital</div>
  <nav class="nav abs">
    <a class="active">Home</a><a>Services</a><a>White Label Link Building</a><a>Contact Us</a>
  </nav>
  <h1 class="hero-title abs">Search Marketing That<br>Actualy Delivers</h1>
  <p class="hero-sub abs">Serach marketing is our forte. Our client results highlight just how good we do it.</p>
</section>

<!-- Welcome -->
<div class="welcome-photo abs" role="img" aria-label="Photo of colleagues reviewing documents at a desk"></div>
<h2 class="welcome-title heading abs">Welcome to Kolvex Digital Ltd.</h2>
<p class="welcome-lead lead abs">Do you want to see an enviable ROI on search marketing?<br>It’s possible – you’ve found us.</p>
<p class="welcome-copy body-copy abs">We know and understand the world of business. We know that ROI is the single most important metric in the marketing world. We’ve worked within some of the world’s largest industries – such as finance, insurance, payday loans and health; where achieving above 100% ROI is often impossible. For us, it’s just a challenge that can be overcome.</p>
<a class="btn" style="left:78px;top:1045px;width:206px;height:45px">Know More <svg viewBox="0 0 22 16" fill="none" stroke="currentColor" stroke-width="2.4"><path d="M1 8h19M13 1l7 7-7 7"/></svg></a>

<!-- Services -->
<div class="grey-band abs"></div>
<section class="services abs">
  <h2 class="services-title heading abs" style="color:var(--white)">Our Services</h2>

  <div class="service abs" style="left:19px;top:120px">
    <svg viewBox="0 0 60 60" fill="none" stroke="#fff" stroke-width="2.4"><circle cx="26" cy="26" r="15"/><path d="M37 37l15 15"/><path d="M20 22a7 7 0 0 1 7-5"/></svg>
    <h3>Organic Search</h3>
    <p>Attract traffic that converts and interacts with your brand through Organic. We implement both short-term and long-term campaigns to bolster your success.</p>
  </div>
  <div class="service abs" style="left:378px;top:120px">
    <svg viewBox="0 0 60 60" fill="none" stroke="#fff" stroke-width="2.4"><rect x="8" y="6" width="44" height="48"/><path d="M8 16h44"/><circle cx="30" cy="34" r="10"/><path d="M30 28v12M27 31h5M27 37h5"/></svg>
    <h3>Paid Search</h3>
    <p>Drive highly converting traffic to your website. Our PPC campaigns are ROI-driven from the start – helping you to scale your business quickly.</p>
  </div>
  <div class="service abs" style="left:737px;top:120px">
    <svg viewBox="0 0 60 60" fill="none" stroke="#fff" stroke-width="2.4"><rect x="6" y="12" width="48" height="36"/><path d="M22 36l16-12M18 30a6 6 0 0 1 0-8l4-4a6 6 0 0 1 8 0M42 30a6 6 0 0 1 0 8l-4 4a6 6 0 0 1-8 0"/></svg>
    <h3>Link Outreach</h3>
    <p>The core foundation of any search campaign. Our team of link outreachers are the best in the industry. We secure link placements that drive rankings.</p>
  </div>

  <div class="service abs" style="left:19px;top:400px">
    <svg viewBox="0 0 60 60" fill="none" stroke="#fff" stroke-width="2.4"><rect x="8" y="10" width="44" height="34"/><path d="M22 54h16M30 44v10M16 20h12M16 28h20M16 36h8"/><circle cx="42" cy="22" r="4"/></svg>
    <h3>UX &amp; CRO</h3>
    <p>Let us dig into your analytic channels and identify where we can bolster your conversion rates while improving user experience.</p>
  </div>
  <div class="service abs" style="left:378px;top:400px">
    <svg viewBox="0 0 60 60" fill="none" stroke="#fff" stroke-width="2.4"><path d="M6 26l24-18 24 18v26H6z"/><path d="M6 26l24 16 24-16"/><path d="M18 18h24v14"/></svg>
    <h3>Email Marketing</h3>
    <p>Our targeted email marketing campaigns allow you to segment users and deliver custom-tailored campaigns and promotions to different demographics.</p>
  </div>
  <div class="service abs" style="left:737px;top:400px">
    <svg viewBox="0 0 60 60" fill="none" stroke="#fff" stroke-width="2.4"><rect x="10" y="10" width="32" height="44"/><path d="M18 6h16v8H18zM16 24h20M16 32h20M16 40h12M48 14v34l-3 6-3-6V14z"/></svg>
    <h3>Social Media</h3>
    <p>Your followers are your most loyal customers. Let us develop a comprehensive strategy that aligns your brand with interests, while driving increased sales.</p>
  </div>

  <a class="btn light" style="left:442px;top:670px;width:206px;height:46px">Know More <svg viewBox="0 0 22 16" fill="none" stroke="currentColor" stroke-width="2.4"><path d="M1 8h19M13 1l7 7-7 7"/></svg></a>
</section>

<!-- Handle SEO -->
<h2 class="seo-title heading abs">Handle SEO Yourself? Perfect.</h2>
<p class="seo-lead lead abs">Hassle-Free Link Placements That Drive Rankings</p>
<p class="seo-copy body-copy abs">Our link placements are used by some of the world’s largest companies in the most difficult industries – such as payday loans, insurance, finance, health and legal. We use our link placement service in conjunction with our Organic Search (SEO) offerings; although some of our clients handle their SEO in-house and prefer to use our link placements to bolster their rankings.</p>
<a class="btn" style="left:78px;top:2331px;width:206px;height:45px">Know More <svg viewBox="0 0 22 16" fill="none" stroke="currentColor" stroke-width="2.4"><path d="M1 8h19M13 1l7 7-7 7"/></svg></a>
<div class="screen-shot abs" role="img" aria-label="Image of the website home page shown on a desktop monitor"></div>

<!-- How it works -->
<h2 class="how-title heading abs">How It Works</h2>
<div class="step abs" style="left:68px;top:2604px">
  <div class="step-icon"><span class="step-num">1</span>
    <svg viewBox="0 0 50 50" fill="none" stroke="#1456a0" stroke-width="2"><rect x="6" y="10" width="38" height="30" rx="3"/><path d="M6 18h38M12 26h20M12 32h14"/></svg></div>
  <h3>You choose your URLs &amp; Anchors</h3>
  <p>With your URLs and anchor text in hand, our team of outreach specialists get to work finding the most authoritative websites.</p>
  <a>READ MORE</a>
</div>
<div class="step abs" style="left:430px;top:2604px">
  <div class="step-icon"><span class="step-num">2</span>
    <svg viewBox="0 0 50 50" fill="none" stroke="#1456a0" stroke-width="2"><circle cx="25" cy="25" r="17"/><path d="M8 25h34M25 8c-8 9-8 25 0 34M25 8c8 9 8 25 0 34"/></svg></div>
  <h3>We handle the outreach</h3>
  <p>With your URLs and anchor text in hand, our team of outreach specialists get to work finding the most authoritative websites.</p>
  <a>READ MORE</a>
</div>
<div class="step abs" style="left:789px;top:2604px">
  <div class="step-icon"><span class="step-num">3</span>
    <svg viewBox="0 0 50 50" fill="none" stroke="#1456a0" stroke-width="2"><rect x="10" y="8" width="30" height="36"/><path d="M18 4h14v8H18zM16 22h18M16 29h18M16 36h10"/></svg></div>
  <h3>You get a full report</h3>
  <p>With your URLs and anchor text in hand, our team of outreach specialists get to work finding the most authoritative websites.</p>
  <a>READ MORE</a>
</div>

<!-- CTA -->
<div class="cta abs" role="img" aria-label="Photo of a team meeting in a dim office"></div>
<div class="cta-tint abs"></div>
<div class="partners abs">
  <span class="badge" style="width:110px"></span>
  <span class="badge" style="width:100px;height:22px"></span>
  <span class="badge" style="width:100px;height:26px"></span>
  <span class="badge" style="width:96px;height:30px"></span>
  <span class="badge" style="width:110px"></span>
  <span class="badge" style="width:92px;height:30px"></span>
</div>
<h2 class="cta-title heading abs" style="color:var(--white)">Want To Improve Your ROI? Let’s Talk</h2>
<p class="cta-sub abs">We’ll never turn down an opportunity to discover how we can help grow your business</p>
<a class="btn light" style="left:463px;top:3263px;width:274px;height:44px">Contact Us Today <svg viewBox="0 0 22 16" fill="none" stroke="currentColor" stroke-width="2.4"><path d="M1 8h19M13 1l7 7-7 7"/></svg></a>

<!-- Contact -->
<h2 class="contact-title heading abs">Contact us</h2>
<div class="field abs" style="left:257px;top:3496px;width:333px;height:46px">Name</div>
<div class="field abs" style="left:619px;top:3496px;width:324px;height:46px">Email</div>
<div class="field abs" style="left:257px;top:3566px;width:333px;height:46px">Phone</div>
<div class="field abs" style="left:619px;top:3566px;width:324px;height:46px">Business name</div>
<div class="field abs" style="left:257px;top:3633px;width:686px;height:99px">Message</div>
<a class="btn" style="left:528px;top:3756px;width:185px;height:46px">Send Now <svg viewBox="0 0 22 16" fill="none" stroke="currentColor" stroke-width="2.4"><path d="M1 8h19M13 1l7 7-7 7"/></svg></a>

<!-- Footer -->
<footer class="footer abs">
  <div class="footer-nav abs">
    <span>Home</span><span class="sep">|</span><span>Services</span><span class="sep">|</span><span>White label link building</span><span class="sep">|</span><span>Contact us</span><span class="sep">|</span><span>Sitemap</span>
  </div>
  <p class="copyright abs">©KOLVEX DIGITAL LTD. 2018 - All Rights Reserved.</p>
</footer>

</body>
</html>
```